Vindmark Health & Wellness needs a fresh and interesting website

I need a rebrand and redevelopment of my website, www.dellaquorne.example
Our mission is provide bespoke , lifestyle medicine , everyone has their own path to health. and we are creating a personalized experience for people to life their life to the fullest
Vindmark - means sea lands
I need an landing page and about page and potentially a few project launch pages , I have been using Wordpress for my basic information and then I use Plovix for the launch pages of my programs since I can edit those easily.

Target Market(s)

Corporate and individual's who are interested in a different perspective on health and wellness , and living with a chronic illness

Industry/Entity Type

Health, lifestyle , wellness coaching and medicine

Coding

Number of Pages Required

Font styles to use
Other font styles liked:
• look into the logo

Requirements
Must have
• the logo I uploaded
Nice to have
• I want a fresh perspective on health, I have bamboo, hibiscus vibes in my logo , but also like more of a water vibe/ I want something earthy but not too boho it needs to be clean
Should not have
• every other holistic health vibe,

```html
<!DOCTYPE html>
<html lang="en">
<head>
<meta charset="utf-8">
<title>Vindmark Health &amp; Wellness</title>
<link href="https://fonts.googleapis.com/css2?family=Cinzel:wght@400;500&family=Montserrat:wght@400;500;600;700;800&display=swap" rel="stylesheet">
<style>
:root{
  --navy:#0f4a6b;
  --ink:#0b2a4a;
  --teal:#13577a;
  --gold:#d4b873;
  --gold-dark:#b48a4c;
  --green:#a8cc7a;
  --green-deep:#8cbf52;
  --mist:#f1f0ed;
  --sand:#efe2c8;
  --text:#2b2b2b;
  --white:#ffffff;
  --star:#e08a2a;
}
*{box-sizing:border-box;margin:0;padding:0}
html,body{width:1200px;height:3927px;overflow:hidden}
body{font-family:"Montserrat",sans-serif;color:var(--text);background:var(--white)}
.page{position:relative;width:1200px;height:3927px;overflow:hidden}
.abs{position:absolute}
.btn{position:absolute;display:flex;align-items:center;justify-content:center;font-weight:700;font-size:14px;letter-spacing:.5px;color:var(--white);text-transform:uppercase;text-decoration:none}
.eyebrow{font-size:17px;letter-spacing:3px;color:#444;text-transform:uppercase}
.section-title{font-family:"Cinzel",serif;font-weight:400;font-size:39px;color:var(--teal);letter-spacing:1px;line-height:1}
.swoosh{position:absolute;height:8px;border-radius:50%;background:var(--green)}

/* header */
.site-header{position:absolute;top:0;left:0;width:1200px;height:81px;background:var(--white);z-index:3}
.brand{position:absolute;display:flex;align-items:center;gap:10px}
.brand-dot{width:34px;height:34px;border-radius:50%;background:var(--teal)}
.brand-name{font-family:"Cinzel",serif;font-size:30px;color:var(--teal);line-height:1}
.main-nav a{position:absolute;top:38px;font-size:13px;color:#555;text-decoration:none;text-transform:uppercase;transform:translateX(-50%)}
.nav-active-line{position:absolute;left:385px;top:62px;width:55px;height:4px;background:var(--green);border-radius:2px}

/* hero */
.hero{position:absolute;top:81px;left:0;width:1200px;height:636px;background:linear-gradient(90deg,#7fb84a 0%,#9cca62 38%,#b7d58a 55%,#c9dfa6 75%,#a9cd74 100%);overflow:hidden}
.hero-title{position:absolute;left:108px;top:168px;font-family:"Cinzel",serif;font-weight:400;font-size:48px;color:var(--teal);line-height:1}
.hero-sub{position:absolute;left:108px;top:222px;font-family:"Cinzel",serif;font-size:45px;color:var(--white);line-height:1}
.hero-text{position:absolute;left:116px;top:286px;width:440px;font-size:17px;line-height:26px;color:var(--white)}
.hero-arrow{position:absolute;top:282px}

/* about */
.about-photo{position:absolute;left:107px;top:796px;width:460px;height:460px;border-radius:50%;border:7px solid var(--green);padding:14px}
.about-photo .photo{width:100%;height:100%;border-radius:50%;background:linear-gradient(180deg,#e9b98a 0%,#d99561 45%,#b98b6a 70%,#d7bda0 100%)}
.about-copy{position:absolute;left:607px;top:828px;width:500px}
.body-text{font-size:15px;line-height:23.5px;color:#222}

/* services */
.services{position:absolute;top:1266px;left:0;width:1200px;height:645px;background:linear-gradient(180deg,var(--mist) 0%,#eeebe5 60%,#ece6dc 100%)}
.service-card{position:absolute;top:1473px;width:291px;height:336px}
.service-card .photo{position:absolute;left:0;top:0;width:291px;height:243px;border-radius:0 48px 0 0}
.service-card .info{position:absolute;left:27px;top:175px;width:247px;height:144px;background:var(--white);border-radius:30px 30px 0 30px;padding:24px 32px 0 32px;box-shadow:0 4px 14px rgba(0,0,0,.06)}
.service-card h3{font-size:17px;font-weight:600;color:var(--ink);margin-bottom:10px}
.service-card p{font-size:9.5px;line-height:15px;color:#555}
.service-card .go{position:absolute;width:46px;height:38px;background:var(--ink);border-radius:22px 0 0 0;display:flex;align-items:center;justify-content:center}
.service-card.featured .info{background:var(--gold-dark);height:158px}
.service-card.featured h3,.service-card.featured p{color:var(--white)}
.service-card.featured .go{background:#f4f0e6}

/* why */
.why{position:absolute;top:1911px;left:0;width:1200px;height:643px;background:linear-gradient(90deg,#0d4d6e 0%,#155877 38%,#4d6e7a 60%,#8a7b5a 80%,#5e6a4a 100%)}
.why .eyebrow{color:var(--white)}
.why .section-title{color:var(--white)}
.why .body-text{color:var(--white)}

/* testimonials */
.testimonial{position:absolute;background:var(--white);border:1px solid #dde6ec;border-bottom:4px solid var(--teal);box-shadow:0 4px 16px rgba(0,0,0,.05);text-align:center}
.stars{color:var(--star);font-size:22px;letter-spacing:2px;line-height:1}
.testimonial blockquote{font-size:14px;line-height:21px;color:#444}
.testimonial .name{font-size:13px;font-weight:600;color:var(--ink)}
.testimonial .company{font-size:9px;color:#777}

/* contact */
.contact{position:absolute;top:3093px;left:0;width:1200px;height:582px;background:linear-gradient(180deg,#efe1c4 0%,#f1e6d0 60%,#ede0c7 100%)}
.contact-title{position:absolute;left:134px;top:3213px;font-size:40px;font-weight:800;color:var(--ink);letter-spacing:.5px}
.contact-item{position:absolute;left:134px;display:flex;align-items:center;gap:14px}
.contact-icon{width:72px;height:72px;border-radius:50%;background:var(--teal);border:3px solid var(--ink);display:flex;align-items:center;justify-content:center}
.contact-item .label{font-size:16px;font-weight:700;color:var(--teal)}
.contact-item .value{font-size:17px;color:#333;margin-top:6px}
.message-form{position:absolute;left:673px;top:3184px;width:407px;height:412px;background:var(--white);padding:30px 42px}
.message-form h4{font-size:20px;font-weight:500;color:var(--ink);letter-spacing:.3px}
.field{position:absolute;left:42px;width:338px;height:38px;border:1px solid #cfcfcf;font-size:10.5px;color:#444;padding:12px 18px}
.send{position:absolute;left:42px;top:327px;width:338px;height:37px;background:#b8d48a;color:var(--white);font-size:10.5px;font-weight:700;display:flex;align-items:center;justify-content:center;letter-spacing:.5px}

/* footer */
.site-footer{position:absolute;top:3675px;left:0;width:1200px;height:252px;background:var(--white)}
.footer-nav a{position:absolute;top:110px;font-size:15px;color:#222;text-decoration:none;text-transform:uppercase;transform:translateX(-50%)}
.copyright{position:absolute;top:162px;left:0;width:1200px;text-align:center;font-size:12.5px;color:#333}
.social{position:absolute;top:196px;left:550px;display:flex;gap:8px}
.social span{width:28px;height:28px;border-radius:50%;border:2px solid var(--teal)}
</style>
</head>
<body>
<div class="page">

<header class="site-header">
  <div class="brand" style="left:106px;top:24px">
    <span class="brand-dot"></span>
    <span class="brand-name">Vindmark</span>
  </div>
  <nav class="main-nav">
    <a style="left:412px">About us</a>
    <a style="left:531px">Services</a>
    <a style="left:642px">Why us</a>
    <a style="left:744px">Blogs</a>
    <a style="left:858px">Resources</a>
  </nav>
  <span class="nav-active-line"></span>
  <a class="btn" style="left:973px;top:24px;width:151px;height:42px;background:var(--gold);font-weight:500;font-size:13px">Contact us</a>
</header>

<section class="hero" role="img" aria-label="Woman meditating cross-legged in a green garden with raised joined hands">
  <h1 class="hero-title">VINDMARK</h1>
  <p class="hero-sub">HEALTH &amp; WELLNESS</p>
  <p class="hero-text">Lorem ipsum dolor sit amet, consectetur adipiscing elit, sed do eiusmod tempor incididunt ut.</p>
  <a class="btn" style="left:116px;top:364px;width:166px;height:44px;background:var(--navy)">Learn more</a>
  <svg class="hero-arrow" style="left:32px" width="20" height="28" viewBox="0 0 20 28"><path d="M16 2 4 14l12 12" fill="none" stroke="#fff" stroke-width="3"/></svg>
  <svg class="hero-arrow" style="left:1144px" width="20" height="28" viewBox="0 0 20 28"><path d="M4 2l12 12L4 26" fill="none" stroke="#fff" stroke-width="3"/></svg>
</section>

<section class="about">
  <div class="about-photo"><div class="photo" role="img" aria-label="Woman in a yoga lunge on a beach at sunset"></div></div>
  <div class="about-copy">
    <p class="eyebrow">Our story</p>
    <h2 class="section-title" style="margin-top:10px">ABOUT VINDMARK</h2>
    <span class="swoosh" style="left:0;top:80px;width:140px;height:6px"></span>
    <p class="body-text" style="margin-top:40px">At a young age, I discovered the transformative power of Eastern Medicine when it helped me overcome lung concerns, propelling me toward my dreams as a young athlete. Years later, I faced a pivotal choice: How could I best serve and heal my community? The answer was crystal clear—Eastern Medicine.</p>
    <p class="body-text" style="margin-top:23px">As an Eastern Medicine doctor, I've had the privilege of positively impacting my community through integrative health choices.</p>
  </div>
  <a class="btn" style="left:607px;top:1153px;width:166px;height:44px;background:var(--gold)">Learn more</a>
</section>

<svg class="abs" style="left:0;top:1250px" width="1200" height="80" viewBox="0 0 1200 80" preserveAspectRatio="none">
  <path d="M0 40C200 60 400 0 600 10S1000 70 1200 30V80H0Z" fill="var(--mist)"/>
</svg>
<section class="services">
  <p class="eyebrow abs" style="left:0;width:1200px;top:76px;text-align:center">What we do</p>
  <h2 class="section-title abs" style="left:0;width:1200px;top:108px;text-align:center">OUR SERVICES</h2>
  <span class="swoosh" style="left:530px;top:158px;width:140px;height:6px"></span>
</section>

<article class="service-card" style="left:122px">
  <div class="photo" role="img" aria-label="Raised hands framing the sun over mountains at dusk" style="background:linear-gradient(180deg,#f0c27a 0%,#d98a3e 45%,#5b3a24 100%)"></div>
  <div class="info"><h3>Wellness Service</h3><p>Lorem ipsum dolor sit amet, consectetur adipiscing elit, sed do eiusmod tempor incididunt ut labore et dolore</p></div>
  <span class="go" style="left:228px;top:281px"><svg width="20" height="14" viewBox="0 0 20 14"><path d="M1 7h17M12 1l6 6-6 6" fill="none" stroke="#fff" stroke-width="1.6"/></svg></span>
</article>
<article class="service-card featured" style="left:457px">
  <div class="photo" role="img" aria-label="Smiling woman outdoors in a sunny park" style="background:linear-gradient(180deg,#8a9a3a 0%,#a6b245 50%,#7fa23a 100%)"></div>
  <div class="info"><h3>Health Coaching</h3><p>Lorem ipsum dolor sit amet, consectetur adipiscing elit, sed do eiusmod tempor incididunt ut labore et dolore</p></div>
  <span class="go" style="left:228px;top:295px"><svg width="20" height="14" viewBox="0 0 20 14"><path d="M1 7h17M12 1l6 6-6 6" fill="none" stroke="#8cbf52" stroke-width="1.6"/></svg></span>
</article>
<article class="service-card" style="left:793px;top:1478px">
  <div class="photo" role="img" aria-label="Stacked stones by a lake at sunrise" style="background:linear-gradient(180deg,#f4d79a 0%,#d9a35a 45%,#6e5440 100%)"></div>
  <div class="info"><h3>Sed ut perspiciatis</h3><p>Lorem ipsum dolor sit amet, consectetur adipiscing elit, sed do eiusmod tempor incididunt ut labore et dolore</p></div>
  <span class="go" style="left:228px;top:281px"><svg width="20" height="14" viewBox="0 0 20 14"><path d="M1 7h17M12 1l6 6-6 6" fill="none" stroke="#fff" stroke-width="1.6"/></svg></span>
</article>

<section class="why" role="img" aria-label="Smiling woman in an orange hoodie jogging in a city park">
  <p class="eyebrow abs" style="left:122px;top:118px">Why us?</p>
  <h2 class="section-title abs" style="left:122px;top:145px">WHY WE ARE</h2>
  <span class="swoosh" style="left:122px;top:192px;width:140px;height:6px"></span>
  <p class="body-text abs" style="left:132px;top:215px;width:500px">At a young age, I discovered the transformative power of Eastern Medicine when it helped me overcome lung concerns, propelling me toward my dreams as a young athlete. Years later, I faced a pivotal choice: How could I best serve and heal my community? The answer was crystal clear—Eastern Medicine.</p>
  <p class="body-text abs" style="left:132px;top:358px;width:500px">As an Eastern Medicine doctor, I've had the privilege of positively impacting my community through integrative health choices.</p>
  <a class="btn" style="left:130px;top:439px;width:164px;height:44px;background:var(--gold)">Learn more</a>
</section>

<section class="testimonials">
  <p class="eyebrow abs" style="left:0;width:1200px;top:2621px;text-align:center">What people says</p>
  <h2 class="section-title abs" style="left:0;width:1200px;top:2656px;text-align:center">TESTIMONIALS</h2>
  <span class="swoosh" style="left:520px;top:2704px;width:140px;height:6px"></span>

  <div class="testimonial" style="left:-300px;top:2772px;width:513px;height:206px"></div>
  <div class="stars abs" style="left:-12px;top:2796px">★★</div>
  <div class="abs" style="left:0;top:2826px;font-size:12.5px;line-height:19px;color:#444;width:200px;white-space:nowrap;overflow:hidden">iste natus error sit voluptatem<br>um, totam rem aperiam, eaque<br>et quasi architecto beatae vitae<br>quia voluptas sit asper”</div>
  <div class="abs" style="left:0;top:2907px;font-size:12px;font-weight:600;color:var(--ink)">Merrin</div>
  <div class="abs" style="left:0;top:2925px;font-size:9px;color:#777">name</div>

  <div class="testimonial" style="left:337px;top:2757px;width:517px;height:232px;padding:24px 30px;border-bottom-color:var(--green)">
    <div class="stars">★★★★★</div>
    <blockquote style="margin-top:12px">“Sed ut perspiciatis unde omnis iste natus error sit voluptatem accusantium doloremque laudantium, totam rem aperiam, eaque ipsa quae ab illo inventore veritatis et quasi architecto beatae vitae dicta sunt explicabo. vatem quia voluptas sit asper”</blockquote>
    <p class="name" style="margin-top:16px">Jonas Merrin</p>
    <p class="company">Company Name</p>
  </div>

  <div class="testimonial" style="left:976px;top:2772px;width:513px;height:206px"></div>
  <div class="stars abs" style="left:1158px;top:2796px">★★</div>
  <div class="abs" style="left:1016px;top:2826px;font-size:12.5px;line-height:19px;color:#444;width:184px;white-space:nowrap;overflow:hidden">“Sed ut perspiciatis unde omnis<br>accusantium doloremque laudan<br>ipsa quae ab illo inventore veritat<br>&nbsp;&nbsp;&nbsp;&nbsp;&nbsp;&nbsp;dicta sunt explicabo. vate</div>
  <div class="abs" style="left:1150px;top:2907px;font-size:12px;font-weight:600;color:var(--ink)">Jonas</div>
</section>

<section class="contact" role="img" aria-label="Soft sand texture with bamboo stalks along the edges"></section>
<h2 class="contact-title">CONTACT US</h2>
<span class="swoosh" style="left:134px;top:3268px;width:140px;height:6px"></span>
<p class="abs" style="left:146px;top:3302px;width:470px;font-size:16px;line-height:25px;color:#333">Lorem ipsum dolor sit amet, consectetur adipiscing elit, sed do eiusmod tempor incididunt ut labore et dolore</p>
<div class="contact-item" style="top:3390px">
  <span class="contact-icon"><svg width="34" height="34" viewBox="0 0 24 24"><path d="M6.6 10.8a15 15 0 0 0 6.6 6.6l2.2-2.2a1 1 0 0 1 1-.25 11.4 11.4 0 0 0 3.6.57 1 1 0 0 1 1 1V20a1 1 0 0 1-1 1A17 17 0 0 1 3 4a1 1 0 0 1 1-1h3.5a1 1 0 0 1 1 1c0 1.25.2 2.45.57 3.57a1 1 0 0 1-.25 1z" fill="none" stroke="#fff" stroke-width="1.3"/></svg></span>
  <div><p class="label">Phone Number</p><p class="value">970-555-0148</p></div>
</div>
<div class="contact-item" style="top:3485px">
  <span class="contact-icon"><svg width="34" height="26" viewBox="0 0 34 26"><rect x="2" y="2" width="30" height="22" fill="none" stroke="#fff" stroke-width="1.6"/><path d="M2 2l15 12L32 2M2 24l11-10M32 24 21 14" fill="none" stroke="#fff" stroke-width="1.6"/></svg></span>
  <div><p class="label">Email address</p><p class="value">info@vindmark.example</p></div>
</div>

<form class="message-form">
  <h4>LEAVE ME A MESSAGE</h4>
  <span class="swoosh" style="left:42px;top:68px;width:60px;height:4px"></span>
  <div class="field" style="top:92px">Name</div>
  <div class="field" style="top:144px">Email address</div>
  <div class="field" style="top:196px">Phone Number</div>
  <div class="field" style="top:246px;height:70px">Message</div>
  <div class="send">SEND MESSAGE</div>
</form>

<footer class="site-footer">
  <nav class="footer-nav">
    <a style="left:172px">About us</a>
    <a style="left:305px">Services</a>
    <a style="left:430px">Why us</a>
    <a style="left:767px">Blogs</a>
    <a style="left:897px">Resources</a>
    <a style="left:1038px">Contact</a>
  </nav>
  <div class="brand" style="left:514px;top:78px;flex-direction:column;gap:8px">
    <span class="brand-dot"></span>
    <span class="brand-name" style="font-size:34px">Vindmark</span>
  </div>
  <p class="copyright">© 2024 Company Name | All Rights Reserved</p>
  <div class="social"><span></span><span></span><span></span></div>
</footer>

</div>
</body>
</html>
```